Ashworth Web Design Project

I need the front page and an internal page designed for this client's website. The logo is attached. Obviously the colors have to go with and/or work with the logo colors. I also attached a very rough brochure layout to help you see the direction we're going in with print materials. The rough site map is also attached. I see a slider on the homepage, the art for which I may come back to you to create. This clinic is in a very high end Dallas neighborhood. The hook is that it's a primary care and urgent facility with convenient hours.

I don't know how much this impacts your design, but this will be a Wordpress site and I'm using a framework called Struxo (struxo-demo.example). If Struxo proves to be inflexible, I'll have to get a template that allows me to execute your design.

This site (http://oakbendcareclinic.example) has the type and quality of content I will eventually have on the Ashworth site.

I just revised the brief for this project. I added the site map and added details to the overview and the "Must Have" section. Thank you for revisiting the brief. 

Reason: Christmas was a bad time to end it.

Target Market(s)

Women 25-54 with children living at home, income over $150k/year

Industry/Entity Type

Clinic

Requirements
Must have
• Masthead incorporating the logo
Followed by the primary nav
Slider on the home page below that
Dual nav - 1 with the nav in the attached site map
2 secondary nav with areas of healthcare
There will three blocks under the nav
1. It's about time (with a small blurb less than 50 words.
2. It's about choices (with small blurb)
3. It's about you (with small blurb)
Three footer blocks
patient check in link on every page
"No appointment? No problem" icon on every page

```html
<!DOCTYPE html>
<html lang="en">
<head>
<meta charset="utf-8">
<title>Ashworth Medical – Immediate Family and Personal Care</title>
<link rel="stylesheet" href="https://fonts.googleapis.com/css2?family=Arimo:wght@400;700&display=swap">
<style>
:root{
  --blue:#1463a8;
  --blue-light:#3b8fe0;
  --green:#17b35a;
  --green-light:#2ed27a;
  --green-pale:#cdeedb;
  --text:#333;
  --muted:#555;
  --band-top:#ffffff;
  --band-bottom:#c6cfe8;
  --line:#1463a8;
}
*{box-sizing:border-box;margin:0;padding:0}
html,body{width:1200px;height:1200px;overflow:hidden;background:#fff}
body{position:relative;font-family:"Arimo",Arial,sans-serif;color:var(--text)}
.top-rule{position:absolute;left:0;top:0;width:1200px;height:2px;background:var(--green)}
.header-band{position:absolute;left:0;top:2px;width:1200px;height:398px;background:linear-gradient(to bottom,var(--band-top) 0%,#fff 35%,var(--band-bottom) 100%)}
.account-tab{position:absolute;left:915px;top:0;width:150px;height:30px;background:var(--green);border-radius:0 0 5px 5px;color:#fff;font-size:11px;display:flex;align-items:center;justify-content:center;gap:6px}
.brand{position:absolute;left:130px;top:30px;display:flex;align-items:center;gap:8px}
.brand-mark{width:40px;height:40px;border-radius:50%;background:var(--blue)}
.brand-name{font-size:25px;font-weight:700;color:var(--blue);line-height:1;letter-spacing:-.5px}
.brand-tag{font-size:8px;color:#444;margin-top:4px;font-weight:700}
.main-nav{position:absolute;left:130px;top:97px;width:860px;height:24px;border-bottom:1px solid var(--line);display:flex}
.main-nav a{font-size:14px;font-weight:700;color:var(--blue);text-decoration:none;margin-right:39px;height:24px}
.main-nav a.current{border-bottom:3px solid var(--blue);height:25px}
.social{position:absolute;left:995px;top:99px;display:flex;gap:5px}
.social span{width:22px;height:22px;border-radius:4px;background:var(--blue)}
.slider{position:absolute;left:130px;top:139px;width:620px;height:240px;border-radius:4px;overflow:hidden;box-shadow:0 1px 3px rgba(0,0,0,.4);background:linear-gradient(100deg,#1a1a1a 0%,#3b3b3b 30%,#8d8d8d 55%,#c9b68a 75%,#5c5446 100%)}
.slide-caption{position:absolute;left:20px;top:38px;width:280px;color:#fff}
.slide-caption h2{font-size:14px;font-weight:700;margin-bottom:3px}
.slide-caption p{font-size:12px;line-height:15px}
.card{position:absolute;left:770px;width:300px;height:111px;background:linear-gradient(#fff,#f1f1f1);border-radius:4px;box-shadow:0 1px 3px rgba(0,0,0,.3);overflow:hidden}
.card-head{height:29px;padding-left:19px;color:#fff;font-size:11px;font-weight:700;line-height:30px}
.card.patients{top:140px}
.card.patients .card-head{background:linear-gradient(var(--blue-light),#1670c8)}
.card.enquiries{top:270px}
.card.enquiries .card-head{background:linear-gradient(var(--green-light),var(--green))}
.card-body{padding:18px 20px;font-size:12px;color:var(--muted);line-height:14px;position:relative}
.checkin{position:absolute;left:190px;top:24px;display:flex;align-items:center;gap:9px;color:var(--blue);font-weight:700;font-size:12px;text-decoration:none}
.checkin svg{flex:none}
.phone{display:flex;align-items:center;gap:6px;margin-top:12px;margin-left:6px;font-size:14px;font-weight:700;color:var(--muted)}
h3.section{position:absolute;top:426px;font-size:14px;font-weight:700;color:var(--blue)}
.care-list{position:absolute;left:148px;top:459px;list-style:none}
.care-list li{font-size:12px;font-weight:700;color:var(--muted);height:19.5px;padding-left:15px;position:relative}
.care-list li::before{content:"";position:absolute;left:1px;top:5px;width:4px;height:4px;border-right:1.3px solid #444;border-top:1.3px solid #444;transform:rotate(45deg)}
.about-photo{position:absolute;left:370px;top:461px;width:201px;height:121px;border:1px solid #ccc;border-radius:5px;padding:3px;background:#fff}
.about-photo div{width:100%;height:100%;background:linear-gradient(90deg,#d9d4cc,#f2f2f2 50%,#7fb7c6)}
.about-text{position:absolute;left:590px;top:459px;width:235px;font-size:12px;line-height:14.5px}
.about-text p+p{margin-top:5px}
.video{position:absolute;left:851px;top:461px;width:182px;height:104px;background:linear-gradient(90deg,#8a7a4a,#b8a978 45%,#e2e2e2 70%,#9a9a90)}
.video .play{position:absolute;left:148px;top:41px}
.video .time{position:absolute;right:0;bottom:0;background:rgba(0,0,0,.7);color:#fff;font-size:10px;font-weight:700;padding:1px 6px}
.video-caption{position:absolute;left:852px;top:573px;width:170px;font-size:10.5px;line-height:13px;color:var(--muted)}
.pillar{position:absolute;top:636px;width:300px;height:146px}
.pillar-title{position:absolute;left:0;top:0;width:77px;text-align:right;color:var(--green);font-size:15px;font-weight:700;line-height:27px;letter-spacing:-.3px}
.pillar-title .big{text-transform:uppercase}
.pillar-mark{position:absolute;left:92px;top:24px;width:24px;height:24px;border-radius:4px;background:var(--green-pale)}
.pillar-rule{position:absolute;left:105px;top:0;height:146px;border-left:1px dotted var(--green)}
.pillar-text{position:absolute;left:133px;top:0;width:165px;font-size:12px;line-height:14.5px}
.pillar-text p+p{margin-top:4px}
.footer-shade{position:absolute;left:130px;top:876px;width:940px;height:24px;background:radial-gradient(ellipse at 50% 0%,rgba(0,0,0,.16),rgba(0,0,0,0) 70%)}
.footer{position:absolute;left:0;top:918px;width:1200px;text-align:center;font-size:11px;color:var(--muted);line-height:13px}
.footer p+p{margin-top:13px}
</style>
</head>
<body>
<div class="top-rule"></div>
<div class="header-band"></div>
<div class="account-tab"><span>Register</span>|<span>Login</span>|<span>Blog</span></div>

<header class="brand">
  <span class="brand-mark"></span>
  <div>
    <div class="brand-name">Ashworth Medical</div>
    <div class="brand-tag">Immediate Family and Personal Care</div>
  </div>
</header>

<nav class="main-nav">
  <a class="current" href="#">Home</a><a href="#">About</a><a href="#">Services</a><a href="#">Staff</a><a href="#">Insurance</a><a href="#">Videos</a><a href="#">Contact Us</a>
</nav>
<div class="social"><span></span><span></span><span></span></div>

<section class="slider" role="img" aria-label="Slide photo: doctor reading a patient folder by window blinds">
  <div class="slide-caption">
    <h2>TITLE OF SLIDE ONE</h2>
    <p>Lorem ipsum dolor sit amet, consectetur adipiscing elit. Praesent porttitor leo at lorem ultrices ac adipiscing mauris fringilla.</p>
  </div>
</section>

<aside class="card patients">
  <div class="card-head">/// FOR PATIENTS</div>
  <div class="card-body">
    <p style="width:160px;margin-top:1px">Lorem ipsum dolor sit amet, consectetur adipiscing elit. Maecenas orci libero.</p>
    <a class="checkin" href="#">
      <svg width="28" height="28" viewBox="0 0 28 28"><circle cx="14" cy="14" r="13" fill="#1670c8"/><circle cx="14" cy="14" r="10" fill="none" stroke="#fff" stroke-width="1.5"/><rect x="10" y="9" width="8" height="10" fill="none" stroke="#fff" stroke-width="1.5"/><path d="M12 13h4M12 16h3" stroke="#fff" stroke-width="1.2"/></svg>
      <span>Patient<br>Check In</span>
    </a>
  </div>
</aside>

<aside class="card enquiries">
  <div class="card-head">/// FOR GENERAL ENQUIRIES</div>
  <div class="card-body">
    <p>We’re here to help you, <b>Immediately.</b></p>
    <div class="phone">
      <svg width="14" height="16" viewBox="0 0 14 16"><path d="M3 1l3 3-2 2c1 2 3 4 5 5l2-2 3 3-2 3C6 15 0 9 1 3z" fill="#555"/></svg>
      <span>- (214) 555 0142</span>
    </div>
  </div>
</aside>

<h3 class="section" style="left:130px">Areas of Healthcare</h3>
<ul class="care-list">
  <li>Immediate Care</li><li>Allergies</li><li>Primary Care</li><li>Women’s Health</li><li>Medical Spa Treatments</li><li>Men’s Health</li><li>Weight Loss</li>
</ul>

<h3 class="section" style="left:370px">About Ashworth Medical</h3>
<div class="about-photo"><div role="img" aria-label="Photo of two smiling doctors with nurses in a clinic hallway"></div></div>
<div class="about-text">
  <p>Lorem ipsum dolor sit amet, consectetur adipiscing elit. Proin in consequat lacus. Fusce at nunc eu dui blandit malesuada. Nulla non pellentesque justo.</p>
  <p>In pulvinar nisl at magna egestas vulputate at non nulla. Vivamus vel odio viverra elit tincidunt viverra non tincidunt justo.</p>
</div>

<h3 class="section" style="left:850px">Interactive Content</h3>
<div class="video" role="img" aria-label="Video still: doctor at a desk in a consultation room">
  <svg class="play" width="24" height="24" viewBox="0 0 24 24"><circle cx="12" cy="12" r="12" fill="#222"/><path d="M9 7l8 5-8 5z" fill="#fff"/></svg>
  <span class="time">2:19</span>
</div>
<p class="video-caption">Lorem ipsum dolor sit amet, consectetur adipiscing elit.</p>

<section class="pillar" style="left:130px">
  <div class="pillar-title">It’s about<br><span class="big">Time</span></div>
  <div class="pillar-mark" role="img" aria-label="Small heart ornament"></div>
  <div class="pillar-rule"></div>
  <div class="pillar-text"><p>Lorem ipsum dolor sit amet, consectetur adipiscing elit. Morbi dictum erat non erat vehicula ornare.</p><p>Suspendisse tempor, ipsum eget rhoncus pellentesque, purus augue luctus nibh, eget sagittis nibh nibh nec lectus. Aliquam vehicula urna sed neque porta interdum.</p></div>
</section>
<section class="pillar" style="left:450px">
  <div class="pillar-title">It’s about<br><span class="big">Choices</span></div>
  <div class="pillar-mark" role="img" aria-label="Small heart ornament"></div>
  <div class="pillar-rule"></div>
  <div class="pillar-text"><p>Lorem ipsum dolor sit amet, consectetur adipiscing elit. Morbi dictum erat non erat vehicula ornare.</p><p>Suspendisse tempor, ipsum eget rhoncus pellentesque, purus augue luctus nibh, eget sagittis nibh nibh nec lectus. Aliquam vehicula urna sed neque porta interdum.</p></div>
</section>
<section class="pillar" style="left:770px">
  <div class="pillar-title">It’s about<br><span class="big">You</span></div>
  <div class="pillar-mark" role="img" aria-label="Small heart ornament"></div>
  <div class="pillar-rule"></div>
  <div class="pillar-text"><p>Lorem ipsum dolor sit amet, consectetur adipiscing elit. Morbi dictum erat non erat vehicula ornare.</p><p>Suspendisse tempor, ipsum eget rhoncus pellentesque, purus augue luctus nibh, eget sagittis nibh nibh nec lectus. Aliquam vehicula urna sed neque porta interdum.</p></div>
</section>

<div class="footer-shade"></div>
<footer class="footer">
  <p>Copyright ©2012 AshworthFamilyMedical.example. All rights reserved</p>
  <p>4420 Ashworth Ave (at Elm Pkwy) Ste 180,<br>Dallas, TX 75225</p>
</footer>
</body>
</html>
```